Business Card Design For Marketing Agnecy LVT

Need business card design for marketing agency.

Dorian Pell
President, CEO
1-555-304-2917
dorian@lumenvaletrewards.net
www.LumenValeTrewards.biz

Back Side:
Boost Sales Using Rewards, Incentives & Giveaways
Get A Free Sample Package

Target Market(s)

B2B

Industry/Entity Type

Marketing

Contact Information for Business Card

Dorian Pell
President, CEO
1-555-304-2917

Back Side:
Get A Free Sample Package

Please note that my current url is OLD DESIGN. I am working on new design and want the business card to match color themes at least on new site. Here is the demo link for new site so you can see the colors I use, etc.

http://pagekilnstudio.example/qx/dorian/lvt_final/index.html

Requirements
Must have
• Please note that my current url is OLD DESIGN. I am working on new design and want the business card to match color themes at least on new site. Here is the demo link for new site so you can see the colors I use, etc.

Nice to have

Should not have

```html
<!DOCTYPE html>
<html lang="en">
<head>
<meta charset="utf-8">
<title>LVT Business Card</title>
<link rel="stylesheet" href="https://fonts.googleapis.com/css2?family=Open+Sans:wght@400;600;700&display=swap">
<style>
  :root {
    --stage: #6f6f6f;
    --brand-blue: #1a73bd;
    --brand-blue-deep: #1565a8;
    --ink-gray: #4a4a4a;
    --swoosh-gray: #58595b;
    --paper: #ffffff;
  }
  * { margin: 0; padding: 0; box-sizing: border-box; }
  html, body { width: 1200px; height: 800px; overflow: hidden; }
  body {
    background: var(--stage);
    font-family: "Open Sans", Arial, sans-serif;
    position: relative;
  }
  .card {
    position: absolute;
    top: 246px;
    width: 536px;
    height: 306px;
    overflow: hidden;
  }
  .card-front { left: 40px; background: var(--paper); }
  .card-back { left: 624px; background: var(--brand-blue); color: var(--paper); text-align: center; }

  .brand-mark {
    display: flex;
    align-items: center;
    gap: 12px;
    font-weight: 700;
    letter-spacing: 1px;
    white-space: nowrap;
  }
  .brand-dot { border-radius: 50%; flex: none; }

  .front-brand {
    position: absolute;
    top: 32px; left: 0; right: 0;
    justify-content: center;
    color: var(--brand-blue);
    font-size: 27px;
  }
  .front-brand .brand-dot { width: 22px; height: 22px; background: var(--brand-blue); }

  .front-rule {
    position: absolute;
    top: 107px; left: 0; right: 0;
    height: 8px;
    background: var(--brand-blue);
  }
  .holder {
    position: absolute;
    top: 138px; left: 0; right: 0;
    text-align: center;
  }
  .holder-name { color: var(--brand-blue); font-size: 18px; font-weight: 700; line-height: 24px; }
  .holder-title { color: var(--ink-gray); font-size: 13px; line-height: 18px; }
  .contact-list {
    position: absolute;
    top: 199px; left: 0; right: 0;
    list-style: none;
    text-align: center;
    font-size: 13px;
    line-height: 19px;
    color: var(--ink-gray);
  }
  .contact-label { color: var(--brand-blue); font-weight: 700; }
  .front-swoosh { position: absolute; left: 0; bottom: 0; width: 536px; height: 60px; }

  .back-pitch {
    position: absolute;
    top: 17px; left: 0; right: 0;
    font-size: 12.5px;
    font-weight: 700;
    line-height: 19px;
  }
  .back-brand {
    position: absolute;
    top: 128px; left: 0; right: 0;
    flex-direction: column;
    gap: 8px;
    font-size: 30px;
    color: var(--paper);
  }
  .back-brand .brand-dot { width: 24px; height: 24px; background: var(--paper); }
  .back-url {
    position: absolute;
    bottom: 14px; left: 0; right: 0;
    font-size: 13px;
    letter-spacing: 1px;
  }
</style>
</head>
<body>
  <section class="card card-front" aria-label="Business card front">
    <div class="brand-mark front-brand">
      <span class="brand-dot"></span>
      <span class="brand-name">LUMEN VALE TREWARDS</span>
    </div>
    <div class="front-rule"></div>
    <div class="holder">
      <p class="holder-name">Dorian Pell</p>
      <p class="holder-title">President, CEO</p>
    </div>
    <ul class="contact-list">
      <li><span class="contact-label">[P]:</span> 1-555-304-2917</li>
      <li><span class="contact-label">[E]:</span> dorian@lumenvaletrewards.net</li>
      <li><span class="contact-label">[W]:</span> www.LumenValeTrewards.biz</li>
    </ul>
    <svg class="front-swoosh" viewBox="0 0 536 60" preserveAspectRatio="none" aria-hidden="true">
      <path d="M0 0 C120 14 300 22 536 20 L536 60 L0 60 Z" fill="var(--swoosh-gray)"/>
      <path d="M0 26 C180 36 360 36 536 4 L536 60 L0 60 Z" fill="var(--paper)"/>
      <path d="M0 36 C200 46 380 42 536 12 L536 60 L0 60 Z" fill="var(--brand-blue)"/>
    </svg>
  </section>

  <section class="card card-back" aria-label="Business card back">
    <p class="back-pitch">Boost Sales Using Rewards, Incentives &amp; Giveaways<br>Get A Free Sample Package</p>
    <div class="brand-mark back-brand">
      <span class="brand-dot"></span>
      <span class="brand-name">LUMEN VALE TREWARDS</span>
    </div>
    <p class="back-url">www.LumenValeTrewards.biz</p>
  </section>
</body>
</html>
```